Mine Engineering Consultancy specializing in
* Pit optimization
* Mine Design
* Scheduling
* Mine Rehabilitation

Industry/Entity Type

Mining

Contact Information for Business Card

RVT Mining Pty Ltd
Derek Holloway
Director/Principle Mining Engineer
Mobile 0413582961
Email derek.holloway@rvtmining-example.com

```html
<!DOCTYPE html>
<html lang="en">
<head>
<meta charset="utf-8">
<title>RVT Mining Pty Ltd – Business Card</title>
<link rel="stylesheet" href="https://fonts.googleapis.com/css2?family=Rubik:wght@400;500;700&display=swap">
<style>
  :root {
    --stage-top: #1484d2;
    --stage-bottom: #0342a3;
    --card-blue: #1a78c9;
    --card-white: #ffffff;
    --ink-navy: #2b2a5c;
    --ink-violet: #4d4a88;
    --brand-blue: #1c6cbf;
    --contact-ink: #eaf3fc;
  }
  * { box-sizing: border-box; margin: 0; padding: 0; }
  html, body { width: 1200px; height: 800px; overflow: hidden; }
  body {
    background: linear-gradient(180deg, var(--stage-top) 0%, var(--stage-bottom) 100%);
    font-family: "Rubik", Arial, sans-serif;
    position: relative;
  }
  .card {
    position: absolute;
    top: 257px;
    width: 500px;
    height: 286px;
    overflow: hidden;
    box-shadow: 0 18px 40px rgba(0, 20, 70, 0.35);
  }
  .card svg.card-shapes { position: absolute; inset: 0; }
  .card--front { left: 70px; background: var(--card-white); }
  .card--back { left: 630px; background: var(--card-blue); }

  .brand {
    position: absolute;
    left: 0; right: 0; top: 0; bottom: 0;
    display: flex;
    align-items: center;
    justify-content: center;
    gap: 12px;
  }
  .brand__dot {
    width: 26px; height: 26px;
    border-radius: 50%;
    background: var(--brand-blue);
  }
  .brand__name {
    color: var(--brand-blue);
    font-size: 30px;
    font-weight: 400;
    letter-spacing: 0.2px;
  }

  .identity {
    position: absolute;
    left: 0; top: 0;
    width: 280px; height: 286px;
    display: flex;
    flex-direction: column;
    justify-content: center;
    align-items: center;
    text-align: center;
    text-transform: uppercase;
    padding-left: 20px;
  }
  .identity__name {
    color: var(--ink-navy);
    font-size: 21px;
    font-weight: 700;
    letter-spacing: 0.3px;
  }
  .identity__title {
    color: var(--ink-violet);
    font-size: 17px;
    font-weight: 400;
    line-height: 1.2;
    margin-top: 3px;
  }

  .contact {
    position: absolute;
    left: 292px; top: 96px;
    list-style: none;
    color: var(--contact-ink);
    font-size: 9px;
    font-weight: 400;
  }
  .contact__item {
    display: flex;
    align-items: center;
    gap: 7px;
    margin-bottom: 14px;
    white-space: nowrap;
  }
  .contact__icon { width: 11px; height: 11px; flex: none; }
</style>
</head>
<body>

  <section class="card card--front" aria-label="Business card front">
    <svg class="card-shapes" viewBox="0 0 500 286" width="500" height="286" aria-hidden="true">
      <polygon fill="var(--card-blue)" points="0,250 160,250 205,215 500,215 500,286 0,286"/>
      <polygon fill="var(--card-blue)" points="0,0 0,0 500,0 500,0 500,0" />
      <polygon fill="var(--card-blue)" points="0,0 300,0 255,40 0,40"/>
    </svg>
    <div class="brand">
      <span class="brand__dot"></span>
      <span class="brand__name">RVT Mining Pty Ltd</span>
    </div>
  </section>

  <section class="card card--back" aria-label="Business card back">
    <svg class="card-shapes" viewBox="0 0 500 286" width="500" height="286" aria-hidden="true">
      <polygon fill="var(--card-white)" points="0,0 215,0 275,70 275,286 0,286"/>
      <polygon fill="var(--card-blue)" points="0,176 40,176 80,286 0,286"/>
    </svg>
    <div class="identity">
      <p class="identity__name">Derek Holloway</p>
      <p class="identity__title">Director/Principle<br>Mining Engineer</p>
    </div>
    <ul class="contact">
      <li class="contact__item">
        <svg class="contact__icon" viewBox="0 0 24 24" aria-hidden="true"><path fill="currentColor" d="M6.6 10.8a15.2 15.2 0 0 0 6.6 6.6l2.2-2.2a1 1 0 0 1 1-.25 11.4 11.4 0 0 0 3.6.57 1 1 0 0 1 1 1V20a1 1 0 0 1-1 1A17 17 0 0 1 3 4a1 1 0 0 1 1-1h3.5a1 1 0 0 1 1 1c0 1.25.2 2.45.57 3.57a1 1 0 0 1-.25 1z"/></svg>
        <span>(Mobile) - 0413582961</span>
      </li>
      <li class="contact__item">
        <svg class="contact__icon" viewBox="0 0 24 24" aria-hidden="true"><path fill="currentColor" d="M2 5h20v14H2zm2 2v.5l8 5 8-5V7zm0 2.8V17h16V9.8l-8 5z"/></svg>
        <span>derek.holloway@rvtmining-example.com</span>
      </li>
    </ul>
  </section>

</body>
</html>
```